Brackenford Solar Project Sign - 36" x 48" color poster

Need a 36" x 48" sign to put next to our solar project. The solar project is installed and we will print this sign on plastic corrugated board and mount as an informational kiosk next to the project. A picture of a similar kiosk is attached. Its is important that the information is easy to understand and aesthetically pleasing. I've uploaded a draft that we did with the information and general idea. The draft is not the correct dimensions and will not scale to the appropriate size. Looking for a professional to do this well. Thank you !!
Target Market(s)
teenage school children and their parents.
Industry/Entity Type
Solar Energy
Requirements
Must have
- technical information included in the draft. Must include the photo of the solar project. Must include the Tallow Brook Solar Logo. Must be scaled to 36" x 48".
Nice to have
- Color scheme that complements the tallow brook solar logo colors
Should not have
- stock photos

```html
<!DOCTYPE html>
<html lang="en">
<head>
<meta charset="utf-8">
<title>Brackenford School District Solar</title>
<link rel="stylesheet" href="https://fonts.googleapis.com/css2?family=Open+Sans:wght@400;600;700&family=Roboto+Condensed:wght@700&display=swap">
<style>
  :root {
    --blue: #2f7abf;
    --blue-dark: #235f98;
    --orange: #f58a1f;
    --green: #5aa832;
    --ink: #333333;
    --grey: #7a7a7a;
    --white: #ffffff;
    --page: #eeeeee;
  }
  * { box-sizing: border-box; margin: 0; padding: 0; }
  html, body { width: 1020px; height: 1200px; overflow: hidden; background: var(--page); }
  body { font-family: "Open Sans", Arial, sans-serif; color: var(--ink); }

  .poster {
    position: absolute; left: 75px; top: 20px;
    width: 870px; height: 1160px;
    background: var(--white);
    overflow: hidden;
  }

  /* header */
  .header { position: absolute; left: 0; top: 0; width: 870px; height: 155px; }
  .header-panel { position: absolute; left: 0; top: 0; }
  .brand {
    position: absolute; left: 62px; top: 44px;
    display: flex; align-items: center; gap: 16px;
  }
  .brand-mark { width: 56px; height: 56px; background: var(--green); flex: none; }
  .brand-name {
    display: flex; flex-direction: column;
    font-family: "Roboto Condensed", Arial, sans-serif; font-weight: 700;
    font-size: 32px; line-height: 34px; color: var(--green);
  }
  .brand-name .line-2 { letter-spacing: 19px; }
  .contact { position: absolute; left: 543px; top: 24px; color: var(--white); }
  .contact-label {
    font-family: "Roboto Condensed", Arial, sans-serif; font-weight: 700;
    font-size: 27px; line-height: 1;
  }
  .contact-phone {
    font-family: "Roboto Condensed", Arial, sans-serif; font-weight: 700;
    font-size: 42px; line-height: 1; margin-top: 4px;
  }
  .contact-web { display: flex; align-items: center; gap: 8px; font-size: 19px; margin-top: 6px; }

  /* hero */
  .hero { position: absolute; left: 0; top: 155px; width: 870px; height: 497px; }
  .hero-photo {
    position: absolute; inset: 0;
    background: linear-gradient(180deg, #4e86c4 0%, #8db5dc 30%, #6b7d8f 42%, #2d3f74 50%, #33477e 62%, #8a8a3c 80%, #b7a85a 100%);
  }
  .hero-title {
    position: absolute; top: 34px; width: 100%; text-align: center;
    font-family: "Roboto Condensed", Arial, sans-serif; font-weight: 700;
    font-size: 42px; color: var(--white); letter-spacing: 0.5px;
  }
  .hero-sub {
    position: absolute; top: 88px; width: 100%; text-align: center;
    font-weight: 700; font-size: 17.5px; line-height: 1.35; color: var(--white);
  }

  /* data band */
  .data-band { position: absolute; left: 0; top: 652px; width: 870px; height: 302px; background: var(--orange); }
  .card { position: absolute; top: 37px; height: 228px; background: var(--white); }
  .card-chart { left: 67px; width: 349px; }
  .card-layers { left: 456px; width: 347px; }
  .layers-art {
    position: absolute; left: 12px; top: 14px; width: 210px; height: 200px;
    background: linear-gradient(180deg, #d9dde2 0%, #b9c9de 40%, #4a4fc0 55%, #c8ccd2 80%, #e9eaec 100%);
  }
  .layer-labels {
    position: absolute; left: 240px; top: 36px; list-style: none;
    font-size: 12px; color: var(--grey); line-height: 1;
  }
  .layer-labels li { height: 24.5px; }

  /* benefits */
  .benefits { position: absolute; left: 72px; top: 980px; list-style: none; }
  .benefits li { display: flex; align-items: center; gap: 14px; height: 34.5px; font-size: 19px; color: var(--ink); }
  .benefits li::before {
    content: ""; width: 9px; height: 9px; border-radius: 50%; background: var(--orange); flex: none;
  }
  .client {
    position: absolute; left: 603px; top: 984px; width: 114px; height: 114px;
    border-radius: 50%; border: 3px solid var(--ink);
    display: flex; align-items: center; justify-content: center;
    font-size: 13px; font-weight: 700; color: var(--ink);
  }

  .footer-bar { position: absolute; left: 0; top: 1146px; width: 870px; height: 11px; display: flex; }
  .footer-bar .blue { width: 670px; background: var(--blue); }
  .footer-bar .orange { flex: 1; background: var(--orange); }
</style>
</head>
<body>
<div class="poster">

  <header class="header">
    <svg class="header-panel" width="870" height="155" viewBox="0 0 870 155">
      <polygon points="401,0 870,0 870,155 401,155 431,77" fill="var(--blue)"/>
    </svg>
    <div class="brand">
      <span class="brand-mark"></span>
      <span class="brand-name"><span>TALLOW BROOK</span><span class="line-2">SOLAR</span></span>
    </div>
    <div class="contact">
      <div class="contact-label">CALL NOW</div>
      <div class="contact-phone">206-555-0147</div>
      <div class="contact-web">
        <svg width="20" height="20" viewBox="0 0 20 20" fill="none" stroke="#fff" stroke-width="1.4">
          <circle cx="10" cy="10" r="8"/><ellipse cx="10" cy="10" rx="3.5" ry="8"/>
          <line x1="2" y1="10" x2="18" y2="10"/>
        </svg>
        <span>www.tallowbrooksolar.com</span>
      </div>
    </div>
  </header>

  <section class="hero">
    <div class="hero-photo" role="img" aria-label="Photo of the ground-mounted solar array in a grassy field with mountains behind"></div>
    <h1 class="hero-title">BRACKENFORD SCHOOL DISTRICT SOLAR</h1>
    <p class="hero-sub">Incentives from Vermont’s net metering program, renewable energy credits and<br>energy savings pay for this project without adding cost to the district or tax payers</p>
  </section>

  <section class="data-band">
    <div class="card card-chart">
      <svg width="349" height="228" viewBox="0 0 349 228" font-family="Open Sans, Arial, sans-serif" font-size="8" fill="#555">
        <g stroke="#dddddd" stroke-width="0.8">
          <line x1="62" y1="18.0" x2="300" y2="18.0"/><line x1="62" y1="31.2" x2="300" y2="31.2"/>
          <line x1="62" y1="44.4" x2="300" y2="44.4"/><line x1="62" y1="57.6" x2="300" y2="57.6"/>
          <line x1="62" y1="70.8" x2="300" y2="70.8"/><line x1="62" y1="84.0" x2="300" y2="84.0"/>
          <line x1="62" y1="97.2" x2="300" y2="97.2"/><line x1="62" y1="110.4" x2="300" y2="110.4"/>
          <line x1="62" y1="123.6" x2="300" y2="123.6"/><line x1="62" y1="136.8" x2="300" y2="136.8"/>
          <line x1="62" y1="150" x2="300" y2="150"/>
        </g>
        <g text-anchor="end">
          <text x="57" y="21">200</text><text x="57" y="34">180</text><text x="57" y="47">160</text>
          <text x="57" y="60">140</text><text x="57" y="74">120</text><text x="57" y="87">100</text>
          <text x="57" y="100">80</text><text x="57" y="113">60</text><text x="57" y="126">40</text>
          <text x="57" y="140">20</text><text x="57" y="153">0</text>
        </g>
        <g>
          <text x="305" y="21">35000</text><text x="305" y="40">30000</text><text x="305" y="59">25000</text>
          <text x="305" y="78">20000</text><text x="305" y="97">15000</text><text x="305" y="115">10000</text>
          <text x="305" y="134">5000</text><text x="305" y="153">0</text>
        </g>
        <text transform="translate(18,84) rotate(-90)" text-anchor="middle">Global Horizontal Irradiance</text>
        <text transform="translate(30,84) rotate(-90)" text-anchor="middle">(kWh/m²)</text>
        <text transform="translate(342,84) rotate(-90)" text-anchor="middle">Expected Energy (kWh)</text>
        <g fill="#3f6fc4">
          <rect x="66" y="93.9" width="12" height="56.1"/><rect x="85.8" y="87.3" width="12" height="62.7"/>
          <rect x="105.7" y="80.7" width="12" height="69.3"/><rect x="125.5" y="72.1" width="12" height="77.9"/>
          <rect x="145.3" y="51" width="12" height="99"/><rect x="165.2" y="60.9" width="12" height="89.1"/>
          <rect x="185" y="43.1" width="12" height="106.9"/><rect x="204.8" y="32.5" width="12" height="117.5"/>
          <rect x="224.6" y="65.5" width="12" height="84.5"/><rect x="244.5" y="90.6" width="12" height="59.4"/>
          <rect x="264.3" y="113.7" width="12" height="36.3"/><rect x="284.2" y="117" width="12" height="33"/>
        </g>
        <polyline fill="none" stroke="#f5b43a" stroke-width="1.5"
          points="72,110.4 91.8,100.5 111.7,87.3 131.5,70.8 151.3,51 171.2,57.6 191,41.1 210.8,37.8 230.6,67.5 250.5,100.5 270.3,123.6 290.2,126.9"/>
        <g text-anchor="end" font-size="7.5">
          <text transform="translate(75,158) rotate(-60)">January</text>
          <text transform="translate(95,158) rotate(-60)">February</text>
          <text transform="translate(115,158) rotate(-60)">March</text>
          <text transform="translate(134,158) rotate(-60)">April</text>
          <text transform="translate(154,158) rotate(-60)">May</text>
          <text transform="translate(174,158) rotate(-60)">June</text>
          <text transform="translate(194,158) rotate(-60)">July</text>
          <text transform="translate(214,158) rotate(-60)">August</text>
          <text transform="translate(234,158) rotate(-60)">September</text>
          <text transform="translate(253,158) rotate(-60)">October</text>
          <text transform="translate(273,158) rotate(-60)">November</text>
          <text transform="translate(293,158) rotate(-60)">December</text>
        </g>
        <rect x="70" y="208" width="14" height="6" fill="#3f6fc4"/>
        <text x="88" y="214">Expected Energy</text>
        <line x1="175" y1="211" x2="190" y2="211" stroke="#f5b43a" stroke-width="1.5"/>
        <text x="194" y="214">Global Horizontal Irradiance</text>
      </svg>
    </div>

    <div class="card card-layers">
      <div class="layers-art" role="img" aria-label="Exploded diagram of the layers of a solar panel"></div>
      <ul class="layer-labels">
        <li>Frame</li><li>Glass</li><li>Encapsulant</li><li>Solar Cells</li>
        <li>Encapsulant</li><li>Backsheet</li><li>Junction Box</li>
      </ul>
    </div>
  </section>

  <ul class="benefits">
    <li>Project provides energy savings to school district</li>
    <li>Provides curriculum opportunity for students</li>
    <li>Solar energy generated without burning fossil</li>
    <li>New powerline provides electricity to snack shack</li>
  </ul>
  <div class="client">BRACKENFORD</div>

  <div class="footer-bar"><span class="blue"></span><span class="orange"></span></div>
</div>
</body>
</html>
```